I need creative and unique business card design using my company logo. Ok to change logo color. We are a small brokerage doing both Real Estate and Mortgage services. Need to have the follow on business card;
1. agent name - Mila Fenton - Realtor
2. cell - 949-555-0182
3. license number - DRE 04917362
4. business name - Brightway Estates & Lending, Inc
5. business office - 626-555-0147
6. business address - 287 W. Larkmoor Ave #214, Arcadia CA 91088
7. business logo - attached (ok to use different color on logo)

```html
<!DOCTYPE html>
<html lang="en">
<head>
<meta charset="utf-8">
<title>Brightway Estates &amp; Lending – Business Card</title>
<link href="https://fonts.googleapis.com/css2?family=Montserrat:wght@300;400;500;700&display=swap" rel="stylesheet">
<style>
  :root{
    --bg:#262626;
    --blue-light:#4b94d4;
    --blue-mid:#3a78c2;
    --blue-deep:#2b5aa6;
    --blue-dark:#244f99;
    --white:#ffffff;
    --white-soft:rgba(255,255,255,.9);
  }
  *{margin:0;padding:0;box-sizing:border-box}
  html,body{width:1200px;height:900px;overflow:hidden;background:var(--bg)}
  body{font-family:'Montserrat',sans-serif;color:var(--white);position:relative}
  .card{
    position:absolute;left:250px;width:700px;height:400px;border-radius:26px;overflow:hidden;
    box-shadow:0 14px 30px rgba(0,0,0,.45);
  }
  .card--back{top:30px;background:linear-gradient(200deg,var(--blue-light) 0%,var(--blue-mid) 45%,var(--blue-deep) 100%)}
  .card--front{top:470px;background:linear-gradient(205deg,var(--blue-light) 0%,var(--blue-mid) 40%,var(--blue-dark) 100%)}

  .pattern-fill{position:absolute;inset:0;
    background:linear-gradient(160deg,rgba(255,255,255,.12) 0%,rgba(255,255,255,0) 45%,rgba(20,60,130,.25) 100%)}
  .back-brand{position:absolute;right:72px;top:168px;display:flex;align-items:center;gap:12px}
  .back-brand__square{width:44px;height:44px;background:var(--white)}
  .back-brand__name{font-weight:500;font-size:15px;letter-spacing:.18em;text-transform:uppercase}

  .agent{position:absolute;right:44px;top:40px;text-align:right}
  .agent__name{font-weight:700;font-size:24px}
  .agent__title{font-weight:300;font-size:15px;margin-top:2px}

  .wordmark{position:absolute;left:46px;top:150px;font-weight:500;color:var(--white)}
  .wordmark__main{font-size:34px;letter-spacing:.32em}
  .wordmark__sub{font-size:12px;letter-spacing:.28em;margin-top:4px}

  .decor{position:absolute;right:40px;top:120px;width:230px;height:230px;
    background:linear-gradient(140deg,var(--blue-dark) 0%,var(--blue-mid) 55%,var(--blue-light) 100%);
    box-shadow:inset 0 0 0 1px rgba(255,255,255,.08)}

  .address{position:absolute;left:46px;top:250px;font-weight:300;font-size:15px;line-height:1.35;color:var(--white-soft)}
  .contacts{position:absolute;left:46px;top:310px;font-weight:300;font-size:15px;color:var(--white-soft)}
  .contacts__row{display:flex;align-items:center;gap:10px;line-height:1.45}
  .contacts__row svg{width:14px;height:14px;flex:none}
  .license{margin-top:6px;padding-left:24px}
</style>
</head>
<body>

<section class="card card--back">
  <div class="pattern-fill" role="img" aria-label="Repeating brand pattern in shades of blue"></div>
  <div class="back-brand">
    <span class="back-brand__square"></span>
    <span class="back-brand__name">Brightway</span>
  </div>
</section>

<section class="card card--front">
  <div class="decor" role="img" aria-label="Large tonal brand decoration"></div>

  <div class="agent">
    <div class="agent__name">Mila Fenton</div>
    <div class="agent__title">Realtor</div>
  </div>

  <div class="wordmark">
    <div class="wordmark__main">BRIGHTWAY</div>
    <div class="wordmark__sub">ESTATES &amp; LENDING, INC</div>
  </div>

  <address class="address" style="font-style:normal">
    287 W. Larkmoor Ave #214,<br>Arcadia CA 91088
  </address>

  <div class="contacts">
    <div class="contacts__row">
      <svg viewBox="0 0 24 24" fill="#fff"><path d="M3 9c0-3 4-5 9-5s9 2 9 5v2h-5V9c-1-.6-2.4-1-4-1s-3 .4-4 1v2H3z"/><rect x="5" y="13" width="14" height="8" rx="1.5"/></svg>
      <span>626-555-0147</span>
    </div>
    <div class="contacts__row">
      <svg viewBox="0 0 24 24" fill="none" stroke="#fff" stroke-width="2"><rect x="6" y="2" width="12" height="20" rx="2"/><line x1="10" y1="18" x2="14" y2="18"/></svg>
      <span>949-555-0182</span>
    </div>
    <div class="license">License number - DRE 04917362</div>
  </div>
</section>

</body>
</html>
```